High end business card design for custom homebuilding company

Looking for a high end business card design that is unique and elegant. Can use embossing, foil printing, laser die cutting, or any high end printing technique or high end paper. Will upload current design so you can see the logo and what we are using currently, but we want something more unique and elegant. I included our logo to help with design.

Target Market(s)

High end custom home buyers of $1.5 million plus homes. Also real estate developers of high end communities.

Industry/Entity Type

Business

Contact Information for Business Card

Double sided. We want something very elegant and expensive looking. We are looking to incorporate a combination of perhaps linen paper or a high end paper, with foil stamping or embossing/debossing to make the card look unique, but still elegant. We tend to use blacks and golds, but are open to any ideas. Looking for creative and unique design.

Colors

Designer to choose colors to be used in the design.

Requirements
Must have
• High end, elegant look. Can use foil, embossing, or high end papers like linen. We want to make the card unique and interesting, but elegant and expensive looking.
Nice to have
• I am including just some cards I saw that looked interesting for one reason or another. I like a clean elegant design and like both the clean white style, and the blacks. So not sure if we want a black design or white. Would like to see both.

```html
<!DOCTYPE html>
<html lang="en">
<head>
<meta charset="utf-8">
<title>Halden Crest Homes – Business Card</title>
<link rel="stylesheet" href="https://fonts.googleapis.com/css2?family=Open+Sans:wght@400;600;700&display=swap">
<style>
  :root {
    --backdrop: #2b2b2b;
    --card: #121212;
    --card-edge: #1a1a1a;
    --gold: #c9bd3c;
    --gold-line: #b5ab2e;
    --text-grey: #a9a9a9;
    --mark-shade: #191919;
  }
  * { margin: 0; padding: 0; box-sizing: border-box; }
  html, body {
    width: 1200px;
    height: 1000px;
    overflow: hidden;
    background: var(--backdrop);
    font-family: "Open Sans", sans-serif;
  }
  .canvas { position: relative; width: 1200px; height: 1000px; }

  .card {
    position: absolute;
    left: 286px;
    width: 656px;
    height: 394px;
    background: radial-gradient(ellipse at 75% 40%, var(--card-edge), var(--card) 70%);
    overflow: hidden;
  }
  .card--front { top: 72px; }
  .card--back { top: 538px; height: 393px; }

  .card__emblem {
    position: absolute;
    border-radius: 50%;
    background: var(--mark-shade);
  }
  .card--front .card__emblem { left: 30px; top: 20px; width: 400px; height: 400px; }
  .card--back .card__emblem { left: 20px; top: 110px; width: 300px; height: 300px; opacity: .8; }

  .wordmark {
    position: absolute;
    display: flex;
    align-items: center;
    gap: 12px;
    color: var(--gold);
    font-weight: 600;
    font-size: 30px;
    letter-spacing: 1px;
    white-space: nowrap;
  }
  .wordmark__dot {
    width: 40px; height: 40px;
    border-radius: 50%;
    background: var(--gold);
  }
  .card--front .wordmark { right: 50px; top: 290px; }
  .card--back .wordmark { right: 46px; top: 308px; }

  .holder-name {
    position: absolute;
    left: 40px; top: 42px;
    color: var(--gold);
    font-weight: 700;
    font-size: 20px;
  }

  .contact {
    position: absolute;
    left: 383px; top: 57px;
    color: var(--text-grey);
    font-size: 14.5px;
    line-height: 18px;
  }
  .contact__group { margin-bottom: 18px; }
  .contact__row { display: flex; align-items: center; gap: 6px; }
  .contact__icon { width: 12px; height: 12px; flex: none; }

  .social { display: flex; gap: 8px; margin-top: -6px; padding-left: 9px; }
  .social__badge { width: 22px; height: 22px; border-radius: 50%; background: var(--gold); }

  .divider {
    position: absolute;
    left: 269px; top: 285px;
    width: 344px; height: 2px;
    background: var(--gold-line);
  }
</style>
</head>
<body>
<main class="canvas">

  <section class="card card--front" aria-label="Card front">
    <div class="card__emblem" role="img" aria-label="Faint debossed brand emblem"></div>
    <div class="wordmark"><span class="wordmark__dot"></span>Halden Crest Homes</div>
  </section>

  <section class="card card--back" aria-label="Card back">
    <div class="card__emblem" role="img" aria-label="Faint debossed brand emblem"></div>
    <h1 class="holder-name">MARCUS WHITLOW</h1>

    <div class="contact">
      <div class="contact__group">
        <div>Unit 3 14-18 Larkin Street,</div>
        <div>Bellmont, WA 6180</div>
      </div>
      <div class="contact__group">
        <div class="contact__row">
          <svg class="contact__icon" viewBox="0 0 12 12"><path d="M2.5 1 4.5 1 5.5 3.5 4 4.5Q5 7 7.5 8L8.5 6.5 11 7.5 11 9.5Q10 11 8 11 1 9 1 3 1 1.5 2.5 1Z" fill="var(--gold)"/></svg>
          <span>00 0000 0000</span>
        </div>
        <div class="contact__row">
          <svg class="contact__icon" viewBox="0 0 12 12"><path d="M2.5 1 4.5 1 5.5 3.5 4 4.5Q5 7 7.5 8L8.5 6.5 11 7.5 11 9.5Q10 11 8 11 1 9 1 3 1 1.5 2.5 1Z" fill="var(--gold)"/></svg>
          <span>00 0000 0000</span>
        </div>
      </div>
      <div class="contact__group">
        <div class="contact__row">
          <svg class="contact__icon" viewBox="0 0 12 12"><rect x="0.5" y="2" width="11" height="8" fill="var(--gold)"/><path d="M0.5 2 6 6.5 11.5 2" fill="none" stroke="#121212" stroke-width="1"/></svg>
          <span>hello@haldencrest.com.au</span>
        </div>
        <div class="contact__row">
          <svg class="contact__icon" viewBox="0 0 12 12"><g fill="none" stroke="var(--gold)" stroke-width="1.2"><circle cx="6" cy="6" r="5"/><ellipse cx="6" cy="6" rx="2.2" ry="5"/><path d="M1 6H11"/></g></svg>
          <span>www.haldencresthomes.com.au</span>
        </div>
      </div>
      <div class="social" aria-label="Social channels">
        <span class="social__badge"></span>
        <span class="social__badge"></span>
        <span class="social__badge"></span>
        <span class="social__badge"></span>
        <span class="social__badge"></span>
      </div>
    </div>

    <div class="divider"></div>
    <div class="wordmark"><span class="wordmark__dot"></span>Halden Crest Homes</div>
  </section>

</main>
</body>
</html>
```